Redhollow Balloon Festival web site design

"Redhollow" Annual Hot Air Balloon Festival. Be sure to spell Balloon proprely! The largest in the state of Texas. In a park setting with sky divers, live concerts, 5K run event, kids fun zones, food vendors, merchandise, fireowrks, arts & crafts, family oriented, very colorful. Would like to establish themselves as the only event of it's kind in the region. Would like to convey that the event is very cost friendly and a unique experience relative to the other family entertainment opportunities in the area. Easy to read! Would like to emulate various features of www.updraftjubilee.com

Target Market(s)

Families. Kids up to 12. Then adults 25 to 80.

Industry/Entity Type

Entertainment

Requirements
Must have
• Ease of use for participants. There will be an area dedicated to each of the following categories: Attendees, Pilots, Vendors, Volunteers, Performers. Directions, event schedule and tickets will be critical call outs. Then details and sign up info for the other 4 categories. Will need a register/login feature.
Nice to have
• Weather conditions feature, countdown to event clock, social media integration to home page, youtube channel with videos of launch, custom static background image to frame header and content area.
Should not have
• Dark dreary colors or hard to read fonts.

```html
<!DOCTYPE html>
<html lang="en">
<head>
<meta charset="utf-8">
<title>Redhollow Balloon Festival – Anatomy of a Hot-Air Balloon</title>
<link href="https://fonts.googleapis.com/css2?family=Arimo:wght@400;700&display=swap" rel="stylesheet">
<style>
  :root {
    --sky-deep: #0a2fd0;
    --sky-mid: #1f56e8;
    --sky-light: #4c8ff0;
    --nav-blue: #1f73d8;
    --nav-blue-dark: #0d55b6;
    --accent-red: #e4170d;
    --accent-orange: #ff5a12;
    --heading-red: #e0141c;
    --body-text: #3a3a3a;
    --panel-white: #ffffff;
    --link-white: #ffffff;
    --frame-grey: #c9c9c9;
  }
  * { box-sizing: border-box; margin: 0; padding: 0; }
  html, body { width: 1200px; height: 756px; overflow: hidden; }
  body {
    position: relative;
    font-family: "Arimo", Arial, sans-serif;
    background: linear-gradient(180deg, var(--sky-mid) 0%, var(--sky-deep) 55%, #0a2bc4 100%);
  }
  .backdrop { position: absolute; }
  .backdrop-left, .backdrop-right {
    top: 0; width: 284px; height: 345px;
    background: radial-gradient(circle at 50% 35%, #f0a23a 0%, #d8452c 22%, #2d7be6 55%, rgba(24,72,220,0) 100%);
  }
  .backdrop-left { left: 0; }
  .backdrop-right { right: 0; width: 283px; }
  .backdrop-top {
    left: 284px; top: 0; width: 633px; height: 72px;
    background: linear-gradient(90deg, #2250d8 0%, #6c6be0 30%, #d96ad0 55%, #4a7be8 80%, #2250d8 100%);
    opacity: .85;
  }
  .brand {
    position: absolute; left: 288px; top: 26px;
    display: flex; align-items: center; gap: 8px;
    font-size: 30px; font-weight: 700; color: var(--link-white);
  }
  .brand-mark { width: 14px; height: 14px; border-radius: 50%; background: var(--link-white); }
  .search {
    position: absolute; left: 816px; top: 50px; width: 101px; height: 18px;
    background: #e9f3fc; border: 1px solid #b7d3ef;
    font-size: 8px; font-style: italic; color: #3a74b8;
    padding: 4px 6px; display: flex; justify-content: space-between; align-items: center;
  }
  .hero {
    position: absolute; left: 284px; top: 71px; width: 633px; height: 225px;
    border: 2px solid var(--panel-white);
    background: linear-gradient(100deg, #c4302a 0%, #f2c21e 30%, #d23c24 50%, #b8902a 70%, #7a1d1a 100%);
  }
  .main-nav {
    position: absolute; left: 284px; top: 296px; width: 633px; height: 31px;
    background: linear-gradient(180deg, var(--nav-blue) 0%, var(--nav-blue-dark) 100%);
    display: flex; list-style: none;
  }
  .main-nav li {
    font-size: 9.5px; font-weight: 700; color: var(--link-white);
    display: flex; align-items: center; padding: 0 0 0 7px; height: 31px;
  }
  .main-nav li.active { background: linear-gradient(180deg, var(--accent-red), var(--accent-orange)); padding: 0 13px; }
  .page {
    position: absolute; left: 284px; top: 327px; width: 633px; height: 396px;
    background: var(--panel-white);
  }
  .article { position: absolute; left: 16px; top: 14px; width: 450px; color: var(--body-text); font-size: 9.2px; line-height: 12px; }
  .article h1 { font-size: 17px; color: var(--heading-red); margin-bottom: 8px; }
  .article p { margin-bottom: 12px; }
  .article p.narrow { width: 300px; }
  .photo { position: absolute; border: 1px solid var(--frame-grey); }
  .photo-balloons { left: 16px; top: 292px; width: 141px; height: 96px; background: linear-gradient(160deg, #dfe7f2, #c9d5e6 60%, #d99a40); }
  .photo-envelope { left: 172px; top: 292px; width: 144px; height: 96px; background: radial-gradient(circle, #f3f6f0, #3f88d8 45%, #2b5fb0); }
  .photo-skydiver { left: 326px; top: 192px; width: 152px; height: 197px; background: linear-gradient(180deg, #e3e6ea 0%, #cfd4da 65%, #6b8c5a 82%, #3d4a55 100%); }
  .cta-button {
    position: absolute; left: 769px; width: 140px; height: 34px; border-radius: 4px;
    background: linear-gradient(180deg, var(--accent-red), var(--accent-orange));
    color: var(--link-white); font-size: 14px; font-weight: 700;
    display: flex; align-items: center; justify-content: center;
  }
  .side-panel {
    position: absolute; left: 769px; top: 462px; width: 140px; height: 254px; border-radius: 4px;
    background: linear-gradient(180deg, #2e93ef, #0f63c8);
    list-style: none; padding-top: 18px;
  }
  .side-panel li { color: var(--link-white); font-size: 12px; font-weight: 700; text-align: center; height: 24px; }
  .footer-nav {
    position: absolute; left: 284px; top: 727px; list-style: none; display: flex;
    font-size: 8.5px; color: var(--link-white);
  }
  .footer-nav li + li::before { content: "|"; margin: 0 4px; }
</style>
</head>
<body>
  <div class="backdrop backdrop-left" role="img" aria-label="Photo of colourful hot air balloons against a blue sky"></div>
  <div class="backdrop backdrop-right" role="img" aria-label="Photo of colourful hot air balloons against a blue sky"></div>
  <div class="backdrop backdrop-top" role="img" aria-label="Close-up photo of a bright balloon envelope"></div>

  <div class="brand"><span class="brand-mark"></span>Redhollow Balloon Festival</div>
  <div class="search">search this site...
    <svg width="8" height="8" viewBox="0 0 10 10"><circle cx="4" cy="4" r="3" fill="none" stroke="#3a74b8" stroke-width="1.4"/><line x1="6.2" y1="6.2" x2="9.5" y2="9.5" stroke="#3a74b8" stroke-width="1.6"/></svg>
  </div>

  <div class="hero" role="img" aria-label="Photo of many glowing hot air balloons inflating at night"></div>

  <ul class="main-nav">
    <li style="padding-left:7px;padding-right:26px">Home</li>
    <li style="padding-right:14px">About Balloons</li>
    <li class="active">Accommodations</li>
    <li style="padding-left:18px;padding-right:20px">Pilot Information</li>
    <li style="padding-right:23px">Photos</li>
    <li style="padding-right:24px">Vendors</li>
    <li style="padding-right:24px">FAQs</li>
    <li>Contact Us</li>
  </ul>

  <main class="page">
    <article class="article">
      <h1>Anatomy of a Hot-Air Balloon</h1>
      <p>Basically, the hot air balloon consists of three parts: envelope, basket, and burner system. It's a fairly simple piece of equipment, and for what it delivers, it is something of a bargain.</p>
      <p>If you look at what is available in flying machines, for instance, you may be surprised to find that ballooning is less than half as expensive as the next class of aircraft, the sailplane.</p>
      <p>Some recent studies have shown that the average price of a new hot air balloon system is about $9,000, but that of a sailplane is $22,000. A piston-driven single-engine airplane with fixed landing gear averages over $31,000, while the same type of plane with retractable gear costs over $64,000. Multi-engine airplanes are three times this price, and helicopters are eight times this price. Turbo-engine aircraft range in the millions.</p>
      <p class="narrow">But relatively inexpensive as it is, the hot air balloon is a carefully conceived and crafted flying machine.</p>
      <p class="narrow">Since there are differences in detail among the balloons made by the various manufacturers, we will confine ourselves primarily to discussing the Skylark T-50, one of the most popular types and sizes of balloon in current use.</p>
    </article>
    <div class="photo photo-balloons" role="img" aria-label="Photo of three hot air balloons in flight"></div>
    <div class="photo photo-envelope" role="img" aria-label="Photo looking up inside a balloon envelope"></div>
    <div class="photo photo-skydiver" role="img" aria-label="Photo of a skydiver with a flag landing above a crowd"></div>
  </main>

  <div class="cta-button" style="top:334px">Festival Facts</div>
  <div class="cta-button" style="top:375px">Schedule</div>
  <div class="cta-button" style="top:416px">Parking information</div>

  <ul class="side-panel">
    <li>Corpoate Parking</li>
    <li>Map</li>
    <li>Attractions</li>
    <li>Festival Tickets</li>
    <li>Sponsor List 2010</li>
    <li>Board of Directors</li>
    <li>Non-Profit Impact</li>
    <li>Volunteers</li>
    <li>Balloon Rides</li>
  </ul>

  <ul class="footer-nav">
    <li>Home</li><li>About Balloons</li><li>Accommodations</li><li>Pilot Information</li><li>Photos</li><li>Vendors</li><li>FAQs</li><li>Contact Us</li>
  </ul>
</body>
</html>
```